Business Card for Marco Tindley Analytics and Marco Tindley Photography

I want a double sided business card: on one side it should be about "Marco Tindley Photography" and on the other side about "Marco Tindley Analytics". You find the logos for these two projects in the attachments. The design of the business card should blend well with the colours and fonts used in the logos and should be quite simple, yet look professional and modern.

In addition to my name, there should be content for a telephone number, e-mail address and website. There should be little icons (for telephone, email and web) before these fields. I do not want a postal mail address field.
Lastly you should indicate that people can contact me in the following languages: Lëtzebuergesch, Deutsch, Français, English, Castellano, Ido
This should be very unobtrusive: either in a small muted font or with little icons (preferably without using flags as flags represent nations, not languages - one possibility would be by using the 2 letter ISO codes).

The design should be delivered in Adobe Illustrator format or something similar that I can edit easily, as it's possible that I will change my e-mail address and domain soon.

I hope this was detailed enough but still leaves you some freedom for designing something nice.

Thank you!
Marco

Industry/Entity Type

Business

Contact Information for Business Card

e-mail address: mjt_@fernpost.example
website: www.marcotindley.example (for Marco Tindley Photography)
website: quarrynet.example/mjt (for Marco Tindley Analytics - this address is likely to change)
phone: +352 648 907 215 (not my real number - I prefer not to publish it on the web)

Requirements
Nice to have
• A speech bubble followed by the 2-letter language codes (lb, de, fr, en, es, io) or even speech bubble icons for every language would be nice and eliminates the need to put text like 'you can contact me in the following languages'.

```html
<!DOCTYPE html>
<html lang="en">
<head>
<meta charset="utf-8">
<title>Marco Tindley business cards</title>
<link rel="stylesheet" href="https://fonts.googleapis.com/css2?family=Cinzel:wght@400&family=Work+Sans:wght@400;600&display=swap">
<style>
  :root {
    --backdrop: #1f1f21;
    --card: #ffffff;
    --orange: #ef7f1a;
    --green: #0fa24a;
    --blue: #1ba3dc;
    --ink: #3a3a3a;
    --muted: #5e5e5e;
    --rule: #4a4a4a;
  }
  * { margin: 0; padding: 0; box-sizing: border-box; }
  html, body { width: 1200px; height: 929px; overflow: hidden; }
  body {
    background: var(--backdrop);
    font-family: "Work Sans", Arial, sans-serif;
    position: relative;
  }
  .card {
    position: absolute;
    width: 600px;
    height: 343px;
    background: var(--card);
    overflow: hidden;
  }
  .card--photography { left: 150px; top: 92px; }
  .card--analytics { left: 450px; top: 494px; }

  /* front: photography */
  .photo-brand {
    position: absolute;
    left: 0; right: 0; top: 118px;
    display: flex; align-items: center; justify-content: center; gap: 12px;
    font-weight: 600; font-size: 30px; color: var(--orange);
    letter-spacing: 0.5px;
  }
  .brand-dot {
    width: 22px; height: 22px; border-radius: 50%; background: var(--orange);
  }
  .photo-url {
    position: absolute; left: 0; right: 0; top: 228px;
    text-align: center; font-size: 15px; color: var(--muted);
  }
  .photo-url span { color: var(--blue); }

  /* back: analytics */
  .analytics-brand {
    position: absolute; right: 40px; top: 46px;
    font-weight: 600; font-size: 22px; color: var(--orange);
  }
  .rule {
    position: absolute; left: 100px; right: 40px; top: 130px;
    height: 1.5px; background: var(--rule);
  }
  .person { position: absolute; left: 100px; top: 76px; }
  .person__name {
    font-family: "Cinzel", Georgia, serif; font-size: 22px; color: var(--orange);
    line-height: 1.1;
  }
  .person__role {
    font-family: "Cinzel", Georgia, serif; font-size: 15px; color: var(--muted);
  }
  .contacts {
    position: absolute; left: 100px; top: 150px;
    list-style: none; font-size: 14.5px; color: var(--ink);
  }
  .contacts li { display: flex; align-items: center; gap: 12px; height: 22px; }
  .contacts svg { width: 14px; height: 14px; flex: none; }
  .languages {
    position: absolute; right: 40px; top: 148px;
    text-align: right; font-size: 13.5px; color: var(--muted); line-height: 1.3;
  }
  .languages__lead { color: var(--orange); font-weight: 600; }
  .swoosh { position: absolute; left: 0; top: 0; }
</style>
</head>
<body>

<section class="card card--photography">
  <div class="photo-brand"><span class="brand-dot"></span>Marco Tindley Photography</div>
  <p class="photo-url">www.<span>marcotindley.example</span></p>
</section>

<section class="card card--analytics">
  <svg class="swoosh" width="600" height="343" viewBox="0 0 600 343" aria-hidden="true">
    <path d="M0,343 L0,318 C180,318 320,282 420,252 C490,232 550,224 600,222 L600,343 Z" fill="var(--green)"/>
    <path d="M0,335 C170,334 320,300 430,268 C500,248 555,240 600,240" fill="none" stroke="#fff" stroke-width="3"/>
    <path d="M0,306 C180,305 315,268 415,238 C485,218 548,208 600,206" fill="none" stroke="var(--orange)" stroke-width="6"/>
    <path d="M0,343 L0,330 C40,334 80,338 115,343 Z" fill="var(--orange)"/>
  </svg>

  <div class="analytics-brand">Marco Tindley Analytics</div>

  <div class="person">
    <p class="person__name">DANIEL BROOKE</p>
    <p class="person__role">FOUNDER</p>
  </div>
  <div class="rule"></div>

  <ul class="contacts">
    <li>
      <svg viewBox="0 0 14 14"><rect x="3" y="1" width="8" height="12" rx="1.5" fill="none" stroke="var(--green)" stroke-width="1.5"/></svg>
      +352 648 907 215
    </li>
    <li>
      <svg viewBox="0 0 14 14"><rect x="1" y="3" width="12" height="8" fill="var(--green)"/><path d="M1,3 L7,8 L13,3" fill="none" stroke="#fff" stroke-width="1"/></svg>
      mjt_@fernpost.example
    </li>
    <li>
      <svg viewBox="0 0 14 14"><circle cx="7" cy="7" r="6" fill="var(--green)"/><path d="M1,7 H13 M7,1 V13 M3,3.5 H11 M3,10.5 H11" stroke="#fff" stroke-width="0.8" fill="none"/><ellipse cx="7" cy="7" rx="2.8" ry="6" fill="none" stroke="#fff" stroke-width="0.8"/></svg>
      quarrynet.example/mjt
    </li>
  </ul>

  <div class="languages">
    <p class="languages__lead">You can contact me in:</p>
    <p>Lëtzebuergesch, Deutsch,</p>
    <p>Français, English, Castellano</p>
  </div>
</section>

</body>
</html>
```